Create a MAIN PAGE that is so enticing they won't say no. -Velm Kor website

High traffic site but we are not closing the deal as much as we should. Our retention rate is 90%. We believe that our site is not properly conveying to our clients the wonderous, exotic and unique experiences we provide them. Our site must give the same impression we give in person. We are seeking a designer to revise our main page & booking pages as these are our calling card pages.
Our industry is selling fantasy and escapism. We want our main page to convey two high class, discreet, sexy dominatrix's.
We want our booking page to be user friendly.
www.quorvelstudio.example

Target Market(s)

Adult Men ages 45-65

Industry/Entity Type

Sex

Coding

Coded - Design and coding required

Number of Pages Required

2 page

Font styles to use
Serif

Colors
EB3D1F
EC4F4E
F09395
F8D3D4
FCEDEE

Requirements
Must have
• Black & Red color theme, animation, clean, classy, sexy
Nice to have
• Smoke effect on the main page
Should not have
• Should not look basic

```html
<!DOCTYPE html>
<html lang="en">
<head>
<meta charset="utf-8">
<title>Velm Kor — Tag Team Duo</title>
<link href="https://fonts.googleapis.com/css2?family=Anton&family=Arimo:wght@400;700&display=swap" rel="stylesheet">
<style>
:root{
  --black:#000000;
  --ink:#141213;
  --red:#e31515;
  --white:#ffffff;
  --smoke:#bfbfbf;
  --stage:#2e2b2c;
  --display:"Anton", "Impact", sans-serif;
  --body:"Arimo", "Arial", sans-serif;
}
*{margin:0;padding:0;box-sizing:border-box}
html,body{width:1200px;height:4324px;overflow:hidden;background:var(--black)}
body{position:relative;font-family:var(--body);color:var(--white)}
.abs{position:absolute}

/* hero */
.hero{left:0;top:0;width:1200px;height:960px;background:var(--black)}
.hero-red{left:621px;top:0;width:579px;height:960px;background:var(--red)}
.hero-smoke{left:0;top:620px;width:621px;height:340px;
  background:radial-gradient(ellipse at 30% 75%,rgba(220,220,220,.75),rgba(120,120,120,.35) 45%,rgba(0,0,0,0) 75%)}
.menu{left:104px;top:62px;display:flex;align-items:center;gap:10px;font-size:15px;letter-spacing:.5px}
.logo{font-family:var(--display);color:var(--white);font-size:34px;letter-spacing:2px;text-transform:uppercase}
.hero-logo{left:0;width:1200px;top:58px;text-align:center}
.cart{left:1070px;top:66px}
.hero-photo{left:430px;top:265px;width:360px;height:570px;
  background:linear-gradient(180deg,#2a2a2a,#111 60%,#1d1d1d);border-radius:60px 60px 20px 20px}
.hero-title{font-family:var(--display);line-height:1;color:var(--white);text-transform:uppercase}
.t-tag{left:283px;top:318px;font-size:126px}
.t-team{left:578px;top:410px;font-size:126px}
.t-duo{left:454px;top:560px;font-size:158px}

/* packages */
.packages{left:0;top:960px;width:1200px;height:832px;
  background:radial-gradient(ellipse at 55% 40%,#2c2a2b,#161415 55%,#0d0c0c)}
.section-head{font-family:var(--display);text-transform:uppercase;font-size:50px;line-height:58px;color:var(--white)}
.pk-head{left:134px;top:1128px}
.pk-intro{left:567px;top:1128px;width:490px;font-size:15px;line-height:20px}
.card{top:1337px;width:305px;height:308px;padding:40px 36px 0 40px}
.card.solid{background:var(--red)}
.card.outline{border:1px solid var(--red)}
.card h3{font-family:var(--display);font-weight:400;font-size:19px;text-transform:uppercase;margin-bottom:22px;letter-spacing:.3px}
.card p{font-size:14.5px;line-height:20px;width:205px}
.card .book{position:absolute;left:44px;top:227px;width:103px;height:28px;border:1.5px solid var(--white);
  font-family:var(--display);font-size:14px;text-align:center;line-height:25px;text-transform:uppercase}

/* reviews */
.reviews{left:0;top:1792px;width:1200px;height:591px;background:var(--red)}
.rv-photo{left:75px;top:1938px;width:277px;height:503px;
  background:linear-gradient(180deg,#3a3a3a,#111 70%,#222);border-radius:50px 50px 12px 12px}
.rv-head{left:408px;top:1892px;font-family:var(--display);font-size:56px;line-height:64px}
.quote{left:633px;top:1896px;width:452px;font-size:14.5px;line-height:20px}
.quote cite{display:block;font-style:normal;font-weight:700;margin-top:8px;padding-left:6px}
.offer{left:408px;top:2178px;width:720px;font-family:var(--display);font-size:56px;line-height:64px;letter-spacing:.3px}

/* lists */
.sp-head{left:134px;top:2652px}
.lim-head{left:134px;top:3003px}
.tags{left:500px;width:620px;font-family:var(--display);font-size:26px;text-transform:uppercase;line-height:32px}
.row{position:absolute;left:0;display:flex;gap:18px;white-space:nowrap}
.row span{display:flex;align-items:center;gap:12px}
.row span::before{content:"+";font-family:var(--body);font-weight:400;font-size:38px;line-height:32px}
.indent{position:absolute;left:52px;white-space:nowrap}

/* cta */
.cta{left:0;top:3369px;width:1200px;height:289px;background:var(--red);text-align:center}
.cta h2{font-family:var(--display);font-weight:400;font-size:56px;margin-top:70px}
.cta .btn{display:inline-block;margin-top:24px;width:240px;height:63px;border:1.5px solid var(--white);
  font-family:var(--display);font-size:31px;line-height:60px;text-transform:uppercase}

/* video */
.stage{left:0;top:3658px;width:1200px;height:532px;background:var(--stage)}
.play{left:564px;top:3888px}

/* footer */
.footer{left:0;top:4190px;width:1200px;height:134px;background:var(--black)}
.contact{left:104px;top:4218px;color:var(--red);font-size:12.5px}
.foot-logo{left:0;width:1200px;top:4216px;text-align:center;font-size:28px}
.copy{right:62px;top:4218px;font-size:12.5px}
</style>
</head>
<body>

<div class="abs hero"></div>
<div class="abs hero-red"></div>
<div class="abs hero-smoke" role="img" aria-label="Soft drifting smoke"></div>
<div class="abs menu">
  <svg width="18" height="12" viewBox="0 0 18 12"><path d="M0 1h18M0 6h14M0 11h10" stroke="#fff" stroke-width="1.6"/></svg>
  <span>MENU</span>
</div>
<div class="abs hero-logo logo">Velm Kor</div>
<svg class="abs cart" width="24" height="22" viewBox="0 0 24 22" fill="none" stroke="#fff" stroke-width="1.6">
  <path d="M1 2h4l3 12h12l2-9H7"/><circle cx="10" cy="19" r="1.6"/><circle cx="18" cy="19" r="1.6"/>
</svg>
<div class="abs hero-photo" role="img" aria-label="Two dominatrixes in black outfits and sunglasses standing together"></div>
<div class="abs hero-title t-tag">Tag</div>
<div class="abs hero-title t-team">Team</div>
<div class="abs hero-title t-duo">Duo</div>

<section class="abs packages" role="img" aria-label="Dark photo of a man in a suit with a blindfolded woman"></section>
<h2 class="abs section-head pk-head">Package<br>Sessions</h2>
<p class="abs pk-intro">Our packages are just as unique as your experience with us will be. No need to worry that tiny brain of yours trying to express what it is you are looking for exactly. You came to us because we know what you CRAVE and DESIRE. Raunchy roleplay &amp; titillating adventures await you. Want to add on a few extra naughty fetishes? Click HERE to browse our full Menu.</p>

<div class="abs card solid" style="left:104px">
  <h3>Light BDSM Play</h3>
  <p>If you are new to kink and or just prefer the more sensual<br><br>aspects of BDSM. This session is the one for you!</p>
  <div class="book">Book</div>
</div>
<div class="abs card outline" style="left:445px;padding-top:46px">
  <h3>Intro to Pegging</h3>
  <p>Learn how to prep before the session. Then show up ready to make the fantasy a reality.</p>
  <div class="book" style="top:228px">Book</div>
</div>
<div class="abs card solid" style="left:787px;padding-top:46px">
  <h3>Slut Training</h3>
  <p>First have fun playing dress up with Rhea &amp; Sera, then get into all kinds of naughty roleplay fun during this session.</p>
  <div class="book" style="top:236px">Book</div>
</div>

<section class="abs reviews"></section>
<div class="abs rv-photo" role="img" aria-label="Two dominatrixes posing in boots and black outfits"></div>
<h2 class="abs rv-head">REVIEWS</h2>
<blockquote class="abs quote">"I highly recommend Goddess Sera and Master Rhea. Wow, one of the best experiences of my life. The communication was perfect leading up to the session. I had so many wow moments during the session, and couldn't believe how lucky I was to be there. This is definitely something that I will remember the rest of my life. I can't wait to see them again."
  <cite>Colin M. - Savannah</cite>
</blockquote>
<p class="abs offer">We offer BDSM and Kink double domme sessions for singles and couples. Below are some topics that we can discuss together.</p>

<h2 class="abs section-head sp-head">Specialities</h2>
<div class="abs tags" style="top:2644px">
  <div class="row" style="top:0"><span>Power Play</span><span>S&amp;M</span><span>Bondage</span><span>Medical Play</span></div>
  <div class="row" style="top:58px"><span>Role Play</span><span>Cuckolding</span><span>Sub/Slave Training</span></div>
  <div class="row" style="top:112px"><span>Humiliation</span><span>Sissy Slut Training, Forces</span></div>
  <div class="row" style="top:166px"><span>Feminization</span><span>Stileto &amp; Boot Fetish</span></div>
  <div class="row" style="top:219px"><span>Wrestling o scissor/choke</span><span>Holds only</span></div>
</div>

<h2 class="abs section-head lim-head">Limits/Not<br>Interested<br>So Please<br>Don't</h2>
<div class="abs tags" style="top:3013px">
  <div class="row" style="top:0"><span>Incest Play</span><span>Race Play</span><span>Brown Showers</span></div>
  <div class="row" style="top:57px"><span>Any Sex on our part</span><span>Smoking/Ass Tray Fetish</span></div>
  <div class="row" style="top:117px"><span>No Blowjobs/ No Handjobs (or anything that</span></div>
  <div class="indent" style="top:156px">ends in job.)</div>
</div>

<section class="abs cta">
  <h2>Ready to serve Master &amp; Goddess!</h2>
  <div class="btn">Book Us Here</div>
</section>

<section class="abs stage" role="img" aria-label="Promotional video"></section>
<svg class="abs play" width="70" height="70" viewBox="0 0 70 70">
  <circle cx="35" cy="35" r="33" fill="#e6e6e6" stroke="#111" stroke-width="2"/>
  <path d="M27 21l22 14-22 14z" fill="none" stroke="#111" stroke-width="3" stroke-linejoin="round"/>
</svg>

<footer class="abs footer"></footer>
<div class="abs contact">CONTACT GODDEST MASTER</div>
<div class="abs foot-logo logo">Velm Kor</div>
<div class="abs copy">© 2023 by VelmKorStudio</div>

</body>
</html>
```